Skin Care Branding / Package design

We are a manufacturer of consumable hemp products and have some skin care products we want to group into a brand of its own, under our primary brand which is TurnLo.  our website is www.turnloco-example.com
Our current packaging was developed on the fly with little or no thought given to a sub brand concept.  We have sub branded other products such as Quiet Arc, Moss Lantern, and Flagon.  While Turnlo appears on the packaging it is not the predominate brand.
The products will be sold in cosmetic stores, health stores, medspas, pharmacies and other upscale stores.  We want the appeal to be elegant & upscale and stand out on the shelf.
We are open to changing the jar, bottle or container and look forward to any recommendations on this.
Later we will need flyers, social media ads, and other graphics.
Our primary goal is to create designs for each of our products that are consistent and create another sub brand.
We are also open to changing the names of these products.
images of the existing products are attached, we plan to add more skin care products.

```html
<!DOCTYPE html>
<html lang="en">
<head>
<meta charset="utf-8">
<title>TurnLo Skin Care – Label Family</title>
<link rel="stylesheet" href="https://fonts.googleapis.com/css2?family=Roboto:wght@300;400;500;700;900&display=swap">
<style>
  :root {
    --stage: #a9a9a9;
    --ink: #0e0e0e;
    --lime: #a6f531;
    --lime-deep: #7fd61b;
    --paper: #f3f4f7;
    --text-light: #ececec;
    --text-dim: #cfcfcf;
  }
  * { box-sizing: border-box; margin: 0; padding: 0; }
  html, body { width: 1200px; height: 800px; overflow: hidden; }
  body {
    background: var(--stage);
    font-family: "Roboto", Arial, sans-serif;
    position: relative;
  }

  /* ---------- tall labels (serum, lotion, roll-on) ---------- */
  .label-tall {
    position: absolute;
    background: var(--ink);
    color: var(--text-light);
    display: flex;
    flex-direction: column;
    align-items: center;
    overflow: hidden;
    border-radius: 3px;
  }
  .label-tall .top-band {
    width: 100%;
    height: 26px;
    background: var(--paper);
    flex: none;
  }
  .tagline {
    background: var(--lime);
    color: #1a1a1a;
    font-size: 9px;
    letter-spacing: 1.4px;
    text-transform: uppercase;
    border-radius: 5px;
    padding: 3px 0;
    text-align: center;
  }
  .product-name {
    font-weight: 700;
    color: #fff;
    line-height: 1;
    text-align: center;
  }
  .product-type {
    background: var(--lime);
    color: #1a1a1a;
    border-radius: 6px;
    padding: 1px 6px;
    font-size: 10px;
    line-height: 1.2;
    margin-top: 5px;
  }
  .spec { text-align: center; }
  .spec-head {
    font-size: 8px;
    letter-spacing: 1px;
    text-transform: uppercase;
    padding: 0 8px 2px;
    border-bottom: 1px solid #777;
    display: inline-block;
  }
  .spec-value { font-size: 10px; margin-top: 3px; color: var(--text-light); }
  .spec-value .divider { display: inline-block; width: 1px; height: 10px; background: #888; margin: 0 5px; vertical-align: -1px; }
  .net-weight { font-size: 7.5px; color: var(--text-light); }

  .wave-foot {
    position: absolute;
    left: 0; right: 0; bottom: 0;
    height: 92px;
  }
  .wave-foot svg { position: absolute; inset: 0; width: 100%; height: 100%; }
  .brand-mark {
    position: absolute;
    left: 0; right: 0; bottom: 22px;
    display: flex;
    justify-content: center;
    align-items: center;
    gap: 5px;
    font-weight: 900;
    font-size: 15px;
    letter-spacing: 1px;
    color: var(--ink);
  }
  .brand-mark .dot { width: 9px; height: 9px; border-radius: 50%; background: var(--ink); }

  /* placements */
  .facial-serum { left: 50px; top: 288px; width: 170px; height: 362px; }
  .calming-lotion { left: 255px; top: 294px; width: 170px; height: 362px; }
  .move-rollon { left: 456px; top: 404px; width: 124px; height: 258px; }

  .facial-serum .tagline, .calming-lotion .tagline { width: 160px; margin-top: 24px; }
  .facial-serum .product-name { font-size: 19px; margin-top: 26px; }
  .calming-lotion .product-name { font-size: 22px; margin-top: 26px; }
  .facial-serum .spec, .calming-lotion .spec { margin-top: 50px; }
  .facial-serum .net-weight, .calming-lotion .net-weight { margin-top: 38px; }

  .move-rollon .top-band { height: 12px; }
  .move-rollon .product-name { font-size: 15px; margin-top: 26px; }
  .move-rollon .product-type { font-size: 9px; }
  .move-rollon .spec { margin-top: 40px; }
  .move-rollon .spec-head { font-size: 7px; border-bottom: 0; }
  .move-rollon .spec-value { font-size: 6.5px; margin-top: 1px; }
  .move-rollon .spec-value .divider { height: 7px; margin: 0 3px; }
  .move-rollon .net-weight { font-size: 6.5px; margin-top: 38px; }
  .move-rollon .wave-foot { height: 66px; }
  .move-rollon .brand-mark { font-size: 12px; bottom: 16px; }

  /* ---------- jar labels ---------- */
  .label-jar {
    position: absolute;
    color: var(--text-light);
  }
  .label-jar > svg { position: absolute; inset: 0; width: 100%; height: 100%; }
  .jar-content {
    position: absolute;
    inset: 0;
    display: flex;
    flex-direction: column;
    align-items: center;
  }
  .jar-specs {
    width: 100%;
    display: flex;
    justify-content: space-between;
    align-items: flex-end;
    padding: 0 40px 0 36px;
    margin-top: 8px;
  }
  .jar-specs .spec-head { font-size: 8px; }
  .jar-specs .spec-value { font-size: 8px; }
  .jar-specs .net-weight { font-size: 7px; text-align: center; line-height: 1.2; }
  .label-jar .brand-mark { position: static; color: #fff; font-size: 12px; margin-top: 8px; }
  .label-jar .brand-mark .dot { background: #fff; width: 7px; height: 7px; }

  .vitamin-c { left: 606px; top: 526px; width: 254px; height: 130px; }
  .vitamin-c .tagline { width: 138px; font-size: 7.5px; font-weight: 500; padding: 1px 0; margin-top: 6px; }
  .vitamin-c .product-name { font-size: 16px; margin-top: 6px; }
  .vitamin-c .product-type { font-size: 10px; margin-top: 2px; }

  .muscle-joint { left: 890px; top: 544px; width: 254px; height: 118px; }
  .muscle-joint .product-name { font-size: 16px; margin-top: 12px; }
  .muscle-joint .product-type { font-size: 10px; margin-top: 2px; }
  .muscle-joint .jar-specs { padding: 0 44px 0 48px; margin-top: 6px; }
</style>
</head>
<body>

  <!-- Facial Serum -->
  <section class="label-tall facial-serum">
    <div class="top-band"></div>
    <p class="tagline">Tone | Hydrate | Soften</p>
    <h2 class="product-name">Facial Serum</h2>
    <p class="product-type">For Beauty</p>
    <div class="spec">
      <span class="spec-head">CBG Infused</span>
      <p class="spec-value">300mg CBG</p>
    </div>
    <p class="net-weight">NET WT .5 OZ / 15G</p>
    <div class="wave-foot">
      <svg viewBox="0 0 170 92" preserveAspectRatio="none" aria-hidden="true">
        <path d="M0 28 Q90 16 170 0 L170 92 L0 92 Z" fill="var(--lime)"/>
        <path d="M0 34 Q90 20 170 8 L170 92 L0 92 Z" fill="var(--paper)"/>
      </svg>
      <div class="brand-mark"><span>TURNLO</span><span class="dot"></span></div>
    </div>
  </section>

  <!-- Calming Lotion -->
  <section class="label-tall calming-lotion">
    <div class="top-band"></div>
    <p class="tagline">Infused Daily Moisturizer</p>
    <h2 class="product-name">Calming</h2>
    <p class="product-type">Lavander Lotion</p>
    <div class="spec">
      <span class="spec-head">CBD + CBG</span>
      <p class="spec-value">50/50 Blend<span class="divider"></span>800mg</p>
    </div>
    <p class="net-weight">4FL OZ / 120ML</p>
    <div class="wave-foot">
      <svg viewBox="0 0 170 92" preserveAspectRatio="none" aria-hidden="true">
        <path d="M0 22 Q90 10 170 0 L170 92 L0 92 Z" fill="var(--lime)"/>
        <path d="M0 28 Q90 14 170 8 L170 92 L0 92 Z" fill="var(--paper)"/>
      </svg>
      <div class="brand-mark"><span>TURNLO</span><span class="dot"></span></div>
    </div>
  </section>

  <!-- Move Roll-On -->
  <section class="label-tall move-rollon">
    <div class="top-band"></div>
    <h2 class="product-name">Move</h2>
    <p class="product-type">Gel Muscle Roll-On</p>
    <div class="spec">
      <span class="spec-head">Cannabiniods</span>
      <p class="spec-value">50/50 Blend Of<span class="divider"></span>6000mg</p>
    </div>
    <p class="net-weight">NET WT 3 OZ / 90G</p>
    <div class="wave-foot">
      <svg viewBox="0 0 124 66" preserveAspectRatio="none" aria-hidden="true">
        <path d="M0 16 Q60 8 124 0 L124 66 L0 66 Z" fill="var(--lime)"/>
        <path d="M0 21 Q60 11 124 6 L124 66 L0 66 Z" fill="var(--paper)"/>
      </svg>
      <div class="brand-mark"><span>TURNLO</span><span class="dot"></span></div>
    </div>
  </section>

  <!-- Vitamin C Cream -->
  <section class="label-jar vitamin-c">
    <svg viewBox="0 0 254 130" preserveAspectRatio="none" aria-hidden="true">
      <rect width="254" height="130" fill="var(--paper)"/>
      <path d="M12 0 Q4 65 12 130 L242 130 Q250 65 242 0 Z" fill="var(--ink)"/>
      <path d="M12 0 Q4 65 12 130" stroke="var(--lime)" stroke-width="3" fill="none"/>
      <path d="M242 0 Q250 65 242 130" stroke="var(--lime)" stroke-width="3" fill="none"/>
    </svg>
    <div class="jar-content">
      <p class="tagline">Brighten + Hydrate</p>
      <h2 class="product-name">Vitamin C</h2>
      <p class="product-type">Cream</p>
      <div class="jar-specs">
        <div class="spec">
          <span class="spec-head">CBG Infused</span>
          <p class="spec-value">For Beauty<span class="divider"></span>300mg CBG</p>
        </div>
        <p class="net-weight">NET WT<br>.5 OZ / 15G</p>
      </div>
      <div class="brand-mark"><span>TURNLO</span><span class="dot"></span></div>
    </div>
  </section>

  <!-- Muscle & Joint Cream -->
  <section class="label-jar muscle-joint">
    <svg viewBox="0 0 254 118" preserveAspectRatio="none" aria-hidden="true">
      <rect width="254" height="118" fill="var(--paper)"/>
      <path d="M30 0 Q16 59 28 118 L222 118 Q236 59 224 0 Z" fill="var(--ink)"/>
      <path d="M30 0 Q16 59 28 118" stroke="var(--lime)" stroke-width="3" fill="none"/>
      <path d="M224 0 Q236 59 222 118" stroke="var(--lime)" stroke-width="3" fill="none"/>
    </svg>
    <div class="jar-content">
      <h2 class="product-name">Muscle &amp; Joint</h2>
      <p class="product-type">Cream</p>
      <div class="jar-specs">
        <div class="spec">
          <span class="spec-head">CBD + CBG</span>
          <p class="spec-value">Full Spectrum<span class="divider"></span>1500mg</p>
        </div>
        <p class="net-weight">NET WT<br>1 OZ / 30G</p>
      </div>
      <div class="brand-mark"><span>TURNLO</span><span class="dot"></span></div>
    </div>
  </section>

</body>
</html>
```